Radiology Department of an Hospital needs PowerPoint Design

The radiology Department performs X-Ray, Computed Tomography and Magnetic Resonance. We need a PowerPoint Design that includes the logo of the Hospital (file included) and our main business messages.

Target Market(s)

Business Presentations

Industry/Entity Type

Medicine

Requirements
Must have
• The logo of the Hospital (check uploaded file)

The name of the department - this is the main message:
"Serviço de Imagiologia - Amadora, Loures"

The slogan of the Department - it should go immediately bellow the name of the department in a smaller font size:
"Porque Vemos Por Dentro"

The main business messages or keywords of the Department:
"Rigor"
"Segurança"
"Proximidade"
Nice to have
• The logo in all pages.
The name of the Department in all pages, with the slogan.
The keywords well visible in the first page and maybe as large watermarks on following pages.

```html
<!DOCTYPE html>
<html lang="pt">
<head>
<meta charset="utf-8">
<title>VitaLuz Hospital – Serviço de Imagiologia</title>
<link href="https://fonts.googleapis.com/css2?family=Lato:wght@400;700;900&display=swap" rel="stylesheet">
<style>
  :root {
    --stage: #141414;
    --teal: #0b5a6e;
    --teal-dark: #07485a;
    --yellow: #f7c300;
    --navy: #1f3d55;
    --ink: #333d44;
    --white: #ffffff;
    --grid: #e6e9ec;
    --band: #4a4a4a;
    --ice: #e3f1f8;
  }
  * { margin: 0; padding: 0; box-sizing: border-box; }
  html, body { width: 1200px; height: 700px; overflow: hidden; background: var(--stage); font-family: "Lato", sans-serif; }
  .slide { position: absolute; width: 576px; height: 322px; background: var(--white); overflow: hidden; }
  .slide--cover { left: 16px; top: 16px; }
  .slide--thanks { left: 608px; top: 16px; }
  .slide--chart { left: 16px; top: 360px; }
  .slide--info { left: 608px; top: 360px; background: linear-gradient(160deg, #f4fafd 0%, var(--ice) 55%, #cfe6f1 100%); }
  .abs { position: absolute; }
  .brand { display: flex; align-items: center; gap: 8px; color: var(--teal); font-weight: 400; line-height: 0.95; }
  .brand__dot { border-radius: 50%; background: var(--teal); flex: none; }
  .brand--light { color: var(--white); }
  .brand--light .brand__dot { background: var(--white); }

  /* cover */
  .cover__brand { left: 32px; top: 80px; font-size: 26px; }
  .cover__brand .brand__dot { width: 44px; height: 44px; }
  .cover__title { left: 36px; top: 152px; width: 290px; color: var(--teal); font-size: 20px; font-weight: 700; line-height: 1.3; }
  .cover__slogan { left: 36px; top: 221px; color: var(--teal); font-size: 16px; }
  .cover__keys { left: 34px; top: 254px; color: var(--teal); font-size: 16.5px; }

  /* thanks */
  .thanks__brand { left: 310px; top: 40px; font-size: 16px; }
  .thanks__brand .brand__dot { width: 26px; height: 26px; }
  .thanks__title { left: 311px; top: 82px; color: var(--teal); font-size: 27px; font-weight: 900; }
  .thanks__copy { left: 312px; top: 122px; width: 215px; font-size: 5px; line-height: 1.55; color: var(--ink); }
  .thanks__copy p { margin-bottom: 6px; }
  .connect { left: 312px; top: 210px; width: 210px; height: 50px; background: var(--teal); color: var(--white); padding: 8px 18px; }
  .connect__label { font-size: 7.5px; font-weight: 700; }
  .connect__row { display: flex; align-items: center; gap: 3px; margin-top: 8px; font-size: 5px; font-weight: 700; }
  .connect__icon { width: 11px; height: 11px; border-radius: 50%; background: var(--yellow); }
  .connect__handle { margin-left: 4px; }

  /* chart slide */
  .chart__title { left: 18px; top: 12px; width: 290px; color: var(--teal); font-size: 19px; font-weight: 900; line-height: 1.25; }
  .chart__brand { left: 448px; top: 8px; font-size: 16px; }
  .chart__brand .brand__dot { width: 26px; height: 26px; }
  .chart__copy { left: 18px; top: 80px; width: 475px; font-size: 6.5px; line-height: 1.6; color: var(--ink); }
  .chart__band { left: 0; bottom: 0; width: 576px; height: 10px; background: var(--band); }

  /* infographic */
  .info__marker { left: 0; top: 12px; width: 7px; height: 20px; background: var(--teal); }
  .info__title { left: 19px; top: 14px; color: var(--teal); font-size: 13px; font-weight: 900; }
  .info__brand { left: 455px; top: 10px; font-size: 15px; }
  .info__brand .brand__dot { width: 24px; height: 24px; }
  .info__band { left: 0; bottom: 0; width: 576px; height: 10px; background: var(--yellow); }
  .callout { width: 170px; }
  .callout h3 { color: var(--teal); font-size: 11px; font-weight: 700; margin-bottom: 3px; }
  .callout p { font-size: 5.6px; line-height: 1.5; color: var(--ink); }
</style>
</head>
<body>

<!-- Cover slide -->
<section class="slide slide--cover">
  <svg class="abs" style="left:0;top:0" width="576" height="322" viewBox="0 0 576 322">
    <defs>
      <clipPath id="cover-clip"><circle cx="440" cy="162" r="160"/></clipPath>
      <linearGradient id="cover-photo" x1="0" y1="0" x2="1" y2="1">
        <stop offset="0" stop-color="#c9d6d8"/>
        <stop offset="0.5" stop-color="#7f97a6"/>
        <stop offset="1" stop-color="#2e4658"/>
      </linearGradient>
    </defs>
    <path d="M352 0 A185 185 0 0 0 362 322 L576 322 L576 0Z" fill="var(--teal)"/>
    <path d="M410 0 C470 -5 560 20 576 40 L576 0Z" fill="var(--yellow)"/>
    <rect x="270" y="0" width="306" height="322" fill="url(#cover-photo)" clip-path="url(#cover-clip)" role="img" aria-label="Photo of a CT scanner room with radiology workstations"/>
  </svg>
  <div class="abs brand cover__brand"><span class="brand__dot"></span><span>VitaLuz<br>Hospital</span></div>
  <h1 class="abs cover__title">Serviço de Imagiologia - Amadora, Loures</h1>
  <p class="abs cover__slogan">Porque Vemos Por Dentro</p>
  <p class="abs cover__keys">Rigor • Segurança • Proximidade</p>
</section>

<!-- Thank you slide -->
<section class="slide slide--thanks">
  <svg class="abs" style="left:0;top:0" width="300" height="322" viewBox="0 0 300 322">
    <defs>
      <linearGradient id="doctor-photo" x1="0" y1="0" x2="1" y2="1">
        <stop offset="0" stop-color="#e9d5cc"/>
        <stop offset="0.5" stop-color="#f3f1ef"/>
        <stop offset="1" stop-color="#d6dee4"/>
      </linearGradient>
    </defs>
    <path d="M0 0 L150 0 A190 190 0 0 1 240 322 L0 322Z" fill="var(--yellow)"/>
    <path d="M0 0 L140 0 A180 180 0 0 1 222 322 L0 322Z" fill="var(--teal)"/>
    <path d="M0 0 L128 0 A170 170 0 0 1 205 322 L0 322Z" fill="url(#doctor-photo)" role="img" aria-label="Photo of a smiling doctor in a white coat with a stethoscope"/>
  </svg>
  <div class="abs brand thanks__brand"><span class="brand__dot"></span><span>VitaLuz<br>Hospital</span></div>
  <h2 class="abs thanks__title">Thank You</h2>
  <div class="abs thanks__copy">
    <p>Lorem ipsum dolor sit amet, consectetur adipiscing elit, sed do eiusmod tempor incididunt ut labore et dolore magna aliqua. Quis ipsum suspendisse ultrices gravida. Risus commodo viverra maecenas accumsan lacus vel facilisis.</p>
    <p>Lorem ipsum dolor sit amet, consectetur adipiscing elit, sed do eiusmod tempor incididunt ut labore et dolore magna aliqua.</p>
    <p>Lorem ipsum dolor sit amet, consectetur adipiscing elit. Risus commodo viverra maecenas accumsan lacus vel facilisis.</p>
  </div>
  <div class="abs connect">
    <div class="connect__label">Connect With Us</div>
    <div class="connect__row">
      <span class="connect__icon"></span><span class="connect__icon"></span><span class="connect__icon"></span><span class="connect__icon"></span>
      <span class="connect__handle">@username</span>
    </div>
  </div>
</section>

<!-- Chart slide -->
<section class="slide slide--chart">
  <svg class="abs" style="left:0;top:0" width="576" height="322" viewBox="0 0 576 322">
    <path d="M305 0 C330 25 360 35 420 42 C500 50 545 62 576 95 L576 0Z" fill="var(--yellow)"/>
    <path d="M318 0 C340 20 368 28 425 34 C500 42 548 55 576 85 L576 0Z" fill="var(--teal)"/>
    <g font-family="Lato, sans-serif" font-size="5.5" font-weight="700" fill="#444">
      <g stroke="var(--grid)" stroke-width="0.6">
        <line x1="60" y1="148" x2="560" y2="148"/><line x1="60" y1="169" x2="560" y2="169"/>
        <line x1="60" y1="190" x2="560" y2="190"/><line x1="60" y1="212" x2="560" y2="212"/>
        <line x1="60" y1="233" x2="560" y2="233"/><line x1="60" y1="254" x2="560" y2="254"/>
        <line x1="60" y1="275" x2="560" y2="275"/>
      </g>
      <text x="42" y="150">$6k</text><text x="42" y="171">$5k</text><text x="42" y="192">$4k</text>
      <text x="42" y="214">$3k</text><text x="42" y="235">$2k</text><text x="42" y="256">$1k</text><text x="42" y="277">$0k</text>
      <g fill="var(--teal)">
        <rect x="67" y="232.6" width="21" height="42.4"/><rect x="121" y="164.8" width="21" height="110.2"/>
        <rect x="175" y="222" width="21" height="53"/><rect x="229" y="186" width="21" height="89"/>
        <rect x="283" y="203" width="21" height="72"/><rect x="337" y="232.6" width="21" height="42.4"/>
        <rect x="391" y="173.2" width="21" height="101.8"/><rect x="499" y="228.4" width="21" height="46.6"/>
      </g>
      <rect x="466" y="164.8" width="9" height="110.2" fill="var(--navy)"/>
      <g fill="var(--yellow)">
        <rect x="88" y="249.6" width="9" height="25.4"/><rect x="142" y="181.7" width="9" height="93.3"/>
        <rect x="196" y="239" width="9" height="36"/><rect x="250" y="203" width="9" height="72"/>
        <rect x="304" y="220" width="9" height="55"/><rect x="358" y="264.4" width="9" height="10.6"/>
        <rect x="412" y="190.2" width="9" height="84.8"/><rect x="445" y="148" width="21" height="127"/>
        <rect x="520" y="260.2" width="9" height="14.8"/>
      </g>
      <text x="74" y="287">2012</text><text x="128" y="287">2013</text><text x="182" y="287">2014</text>
      <text x="236" y="287">2015</text><text x="290" y="287">2016</text><text x="344" y="287">2017</text>
      <text x="398" y="287">2018</text><text x="452" y="287">2019</text><text x="506" y="287">2020</text>
    </g>
  </svg>
  <h2 class="abs chart__title">Lorem Ipsum Dolor Sit Amet Consectetur</h2>
  <div class="abs brand brand--light chart__brand"><span class="brand__dot"></span><span>VitaLuz<br>Hospital</span></div>
  <p class="abs chart__copy">Lorem ipsum dolor sit amet, consectetur adipisicing elit, sed do eiusmod tempor incididunt ut labore et dolore magna aliqua. Duis aute irure dolor in reprehenderit in voluptate velit esse cillum dolore eu fugiat nulla pariatur. Excepteur sint occaecat cupidatat non proident, sunt in culpa qui officia deserunt mollit anim id est laborum.</p>
  <div class="abs chart__band"></div>
</section>

<!-- Infographic slide -->
<section class="slide slide--info">
  <div class="abs info__marker"></div>
  <h2 class="abs info__title">Infographics Title Here</h2>
  <div class="abs brand info__brand"><span class="brand__dot"></span><span>VitaLuz<br>Hospital</span></div>
  <svg class="abs" style="left:0;top:0" width="576" height="322" viewBox="0 0 576 322">
    <g stroke="var(--teal)" stroke-width="0.8" fill="none">
      <path d="M92 77 H240 L258 90"/><path d="M92 140 H200"/><path d="M92 245 H200 L225 232"/>
      <path d="M444 77 H330 L318 88"/><path d="M444 157 H380"/><path d="M444 245 H360 L345 232"/>
    </g>
    <g transform="translate(292 165)" fill="var(--teal)">
      <path id="seg" d="M39.2,-20 L82,-41.8 A92,92 0 0 1 82,41.8 L39.2,20 A44,44 0 0 0 39.2,-20Z"/>
      <use href="#seg" transform="rotate(60)"/><use href="#seg" transform="rotate(120)"/>
      <use href="#seg" transform="rotate(180)"/><use href="#seg" transform="rotate(240)"/>
      <use href="#seg" transform="rotate(300)"/>
      <circle r="36"/>
      <circle r="28" fill="var(--white)"/>
      <circle r="20" fill="var(--teal)"/>
      <g fill="var(--white)" stroke="none">
        <!-- pie -->
        <circle cx="62" cy="0" r="13"/><path d="M62 0 L62 -13 A13 13 0 0 1 75 0Z" fill="var(--teal)"/>
        <!-- pills -->
        <rect x="22" y="-62" width="28" height="11" rx="5.5" transform="rotate(-40 36 -56)"/>
        <!-- clipboard -->
        <rect x="22" y="44" width="18" height="24" rx="2"/>
        <rect x="26" y="50" width="10" height="2" fill="var(--teal)"/><rect x="26" y="55" width="10" height="2" fill="var(--teal)"/><rect x="26" y="60" width="10" height="2" fill="var(--teal)"/>
        <!-- ambulance -->
        <rect x="-46" y="46" width="28" height="16" rx="2"/><circle cx="-40" cy="64" r="3.5"/><circle cx="-24" cy="64" r="3.5"/>
        <rect x="-37" y="49" width="3" height="10" fill="var(--teal)"/><rect x="-40.5" y="52.5" width="10" height="3" fill="var(--teal)"/>
        <!-- medical kit -->
        <rect x="-76" y="-9" width="26" height="20" rx="2"/><rect x="-68" y="-13" width="10" height="5" rx="1"/>
        <rect x="-64.5" y="-5" width="3" height="12" fill="var(--teal)"/><rect x="-69" y="-0.5" width="12" height="3" fill="var(--teal)"/>
        <!-- microscope -->
        <rect x="-38" y="-72" width="6" height="20" rx="1" transform="rotate(30 -35 -62)"/>
        <rect x="-46" y="-44" width="24" height="3"/><rect x="-30" y="-56" width="4" height="12"/>
      </g>
    </g>
  </svg>
  <div class="abs callout" style="left:19px;top:68px"><h3>Icon Text here</h3><p>Duis aute irure dolor in reprehenderit in voluptate velit esse cillum dolore eu fugiat nulla pariatur. Excepteur sint occaecat cupidatat non proident, sunt in culpa qui officia deserunt mollit anim id est laborum.</p></div>
  <div class="abs callout" style="left:19px;top:131px"><h3>Icon Text here</h3><p>Duis aute irure dolor in reprehenderit in voluptate velit esse cillum dolore eu fugiat nulla pariatur. Excepteur sint occaecat cupidatat non proident, sunt in culpa qui officia deserunt mollit anim id est laborum.</p></div>
  <div class="abs callout" style="left:19px;top:236px"><h3>Icon Text here</h3><p>Duis aute irure dolor in reprehenderit in voluptate velit esse cillum dolore eu fugiat nulla pariatur. Excepteur sint occaecat cupidatat non proident, sunt in culpa qui officia deserunt mollit anim id est laborum.</p></div>
  <div class="abs callout" style="left:443px;top:68px;width:128px"><h3>Icon Text here</h3><p>Duis aute irure dolor in reprehenderit in voluptate velit esse cillum dolore eu fugiat nulla pariatur. Excepteur sint occaecat cupidatat non proident, sunt in culpa qui officia deserunt mollit anim id est laborum.</p></div>
  <div class="abs callout" style="left:443px;top:148px;width:128px"><h3>Icon Text here</h3><p>Duis aute irure dolor in reprehenderit in voluptate velit esse cillum dolore eu fugiat nulla pariatur. Excepteur sint occaecat cupidatat non proident, sunt in culpa qui officia deserunt mollit anim id est laborum.</p></div>
  <div class="abs callout" style="left:443px;top:236px;width:128px"><h3>Icon Text here</h3><p>Duis aute irure dolor in reprehenderit in voluptate velit esse cillum dolore eu fugiat nulla pariatur. Excepteur sint occaecat cupidatat non proident, sunt in culpa qui officia deserunt mollit anim id est laborum.</p></div>
  <div class="abs info__band"></div>
</section>

</body>
</html>
```